Dr. Marissa Tevlin Medical/Chiropractic Business Card

Dr. Tevlin is a chiropractor and will require a business card that she uses every single day to book appointments on the back side of the card. Currently the office name goes by Dr. Marissa Tevlin. The chiropractic profession is based on the diagnosis and manipulative treatment of misalignments of the joints, especially those of the spinal column, which are held to cause other disorders by affecting the nerves, muscles, and organs. Dr. Marissa Tevlin is looking for a contemporary and minimalistic design.

Industry/Entity Type

Medical

Contact Information for Business Card

Name: Dr. Marissa Tevlin; Address: 748 Harcastle Rd South, London, ON N5R 2K7; Phone Number: 519.274.6193; Fax: 519.281.5046; email: marissa.tevlin@quorvamail.com

Requirements
Must have
• ability to write multiple appointments date/time on the back of card

```html
<!DOCTYPE html>
<html lang="en">
<head>
<meta charset="utf-8">
<title>Dr. Marissa Tevlin – Business Card</title>
<link rel="stylesheet" href="https://fonts.googleapis.com/css2?family=Montserrat:ital,wght@0,300;0,400;0,600;0,700;1,400&display=swap">
<style>
  :root {
    --ink: #1b1b1b;
    --paper: #ececec;
    --line: #7a7a7a;
    --muted: #6a6a6a;
    --backdrop: #f4f4f4;
    --white: #ffffff;
  }
  * { margin: 0; padding: 0; box-sizing: border-box; }
  html, body {
    width: 1200px; height: 782px; overflow: hidden;
    background: var(--backdrop);
    font-family: "Montserrat", sans-serif;
  }
  .canvas { position: relative; width: 1200px; height: 782px; }

  .card { position: absolute; overflow: hidden; background: var(--paper); }

  /* Front */
  .card-front { left: 254px; top: 226px; width: 314px; height: 544px; }
  .card-front .shapes { position: absolute; inset: 0; }
  .identity { position: absolute; top: 68px; width: 100%; text-align: center; }
  .identity .name {
    font-weight: 700; font-size: 21px; letter-spacing: 0.8px;
    color: var(--ink); text-transform: uppercase;
  }
  .identity .title {
    font-weight: 400; font-size: 12px; letter-spacing: 0.6px;
    color: var(--muted); text-transform: uppercase; margin-top: 1px;
  }
  .contact {
    position: absolute; top: 208px; width: 100%;
    list-style: none; text-align: center;
    font-weight: 400; font-size: 13px; line-height: 16px; color: var(--ink);
  }
  .contact li { display: flex; justify-content: center; align-items: center; gap: 5px; }
  .contact svg { width: 10px; height: 10px; fill: var(--ink); }
  .address {
    position: absolute; top: 396px; width: 100%; text-align: center;
    font-style: normal; font-weight: 400; font-size: 13px; line-height: 17px;
    color: var(--white);
  }

  /* Back */
  .card-back { left: 710px; top: 84px; width: 327px; height: 570px; }
  .card-back .shapes { position: absolute; inset: 0; }
  .appointments-title {
    position: absolute; top: 14px; width: 100%; text-align: center;
    font-weight: 700; font-size: 19px; letter-spacing: 1.2px; color: var(--ink);
  }
  .col-head {
    position: absolute; top: 56px;
    font-weight: 600; font-size: 13px; letter-spacing: 0.8px; color: var(--white);
  }
  .col-date { left: 63px; }
  .col-time { left: 260px; }
  .reschedule-note {
    position: absolute; top: 528px; width: 100%; text-align: center;
    font-style: italic; font-weight: 400; font-size: 12.5px; line-height: 17px;
    color: var(--white);
  }
</style>
</head>
<body>
<main class="canvas">

  <section class="card card-front" aria-label="Business card front">
    <svg class="shapes" viewBox="0 0 314 544" width="314" height="544" aria-hidden="true">
      <rect width="314" height="544" fill="var(--ink)"/>
      <ellipse cx="157" cy="190" rx="150" ry="138" fill="var(--paper)"/>
      <ellipse cx="157" cy="168" rx="162" ry="137" fill="var(--ink)"/>
      <rect width="314" height="199" fill="var(--paper)"/>
      <ellipse cx="157" cy="140" rx="175" ry="150" fill="var(--paper)"/>
    </svg>

    <header class="identity">
      <h1 class="name">Dr. Marissa Tevlin</h1>
      <p class="title">Chiropractor</p>
    </header>

    <ul class="contact">
      <li>
        <svg viewBox="0 0 10 10" aria-hidden="true"><path d="M2 0.5 L3.6 0.5 L4 3 L2.9 3.8 Q3.8 5.9 5.9 7 L6.8 6 L9.3 6.4 L9.3 8.2 Q9 9.5 7.6 9.4 Q1 8.6 0.6 2 Q0.6 0.6 2 0.5 Z"/></svg>
        <span>519.274.6193</span>
      </li>
      <li>
        <svg viewBox="0 0 10 10" aria-hidden="true"><rect x="2.5" y="0.5" width="5" height="3"/><rect x="0.5" y="3.5" width="9" height="4" rx="1"/><rect x="2.5" y="7" width="5" height="2.5"/></svg>
        <span>519.281.5046</span>
      </li>
      <li>
        <svg viewBox="0 0 10 10" aria-hidden="true"><path d="M0.5 2 H9.5 V8 H0.5 Z M1.3 2.7 V7.3 H8.7 V2.7 L5 5.4 Z" fill-rule="evenodd"/></svg>
        <span>marissa.tevlin@quorvamail.com</span>
      </li>
    </ul>

    <address class="address">748 Harcastle Rd South,<br>London, ON N5R 2K7</address>
  </section>

  <section class="card card-back" aria-label="Business card back, appointment log">
    <svg class="shapes" viewBox="0 0 327 570" width="327" height="570" aria-hidden="true">
      <rect x="0" y="46" width="327" height="37" rx="18.5" fill="var(--ink)"/>
      <g stroke="var(--line)" stroke-width="1.3">
        <line x1="0" y1="107" x2="327" y2="107"/>
        <line x1="0" y1="140" x2="327" y2="140"/>
        <line x1="0" y1="173" x2="327" y2="173"/>
        <line x1="0" y1="206" x2="327" y2="206"/>
        <line x1="0" y1="239" x2="327" y2="239"/>
        <line x1="0" y1="272" x2="327" y2="272"/>
        <line x1="0" y1="305" x2="327" y2="305"/>
        <line x1="0" y1="338" x2="327" y2="338"/>
        <line x1="0" y1="371" x2="327" y2="371"/>
        <line x1="0" y1="404" x2="327" y2="404"/>
        <line x1="0" y1="436" x2="327" y2="436"/>
      </g>
      <line x1="208" y1="83" x2="208" y2="468" stroke="var(--ink)" stroke-width="2"/>
      <ellipse cx="163.5" cy="570" rx="255" ry="89" fill="var(--ink)"/>
    </svg>

    <h2 class="appointments-title">APPOINTMENTS</h2>
    <span class="col-head col-date">DATE</span>
    <span class="col-head col-time">TIME</span>

    <p class="reschedule-note">If you are unable to make your appointment,<br>please call us to reschedule</p>
  </section>

</main>
</body>
</html>
```